Lonestar Canopy Services, INC Roof Safety Info Marketing Material

We need a flyer to illustrate roof safety methods we offer with the pictures and descriptions uploaded. We are a Dallas-based commercial roofing company named Lonestar Canopy Services, INC.
We would like to incorporate our dark blues (seen on our website logo). The final design should communicate roof safety and our ability to assess any roof system based on their safety needs.
https://brellwaytops.com/company/about-brellway-tops-inc/

Target Market(s)

Construction industry

Industry/Entity Type

Commercial Roofind

Font styles to use
Serif

```html
<!DOCTYPE html>
<html lang="en">
<head>
<meta charset="utf-8">
<title>Lonestar Canopy Services, INC – Roof Safety Flyer</title>
<link rel="stylesheet" href="https://fonts.googleapis.com/css2?family=Bebas+Neue&family=Poppins:wght@400;500;600;700&display=swap">
<style>
  :root{
    --navy:#173d7f;
    --blue:#2a5a9e;
    --silver:#dfe3ea;
    --panel-grey:#e3e6ea;
    --band-grey:#c9cdd3;
    --green:#8aa63b;
    --alert:#d9312b;
    --ink:#1d1f24;
    --white:#ffffff;
  }
  *{margin:0;padding:0;box-sizing:border-box}
  html,body{width:800px;height:1200px;overflow:hidden;background:var(--white)}
  body{font-family:"Poppins",sans-serif;color:var(--ink)}
  .flyer{position:relative;width:800px;height:1200px;overflow:hidden;background:var(--white)}
  .abs{position:absolute}
  .display{font-family:"Bebas Neue",sans-serif;font-weight:400;white-space:nowrap}

  /* brand */
  .brand{left:40px;top:72px;display:flex;align-items:center;gap:10px}
  .brand-dot{width:20px;height:20px;border-radius:50%;background:var(--navy)}
  .brand-name{font-weight:700;font-size:15px;color:var(--navy);letter-spacing:.2px;white-space:nowrap}

  /* hero */
  .header-art{left:0;top:0}
  .hero-panel{left:0;top:168px;width:382px;height:292px;background:linear-gradient(180deg,var(--navy),var(--blue));padding:26px 0 0 40px;color:var(--white)}
  .hero-kicker{font-size:52px;line-height:.95}
  .hero-title{font-size:76px;line-height:.95;color:var(--silver)}
  .hero-sub{font-size:35px;line-height:1}
  .hero-rule{width:100px;height:3px;background:var(--white);margin:10px 0 12px}
  .hero-copy{font-size:14px;line-height:1.2;width:330px}

  .info-band{left:0;top:460px;width:800px;height:44px}
  .info-band-title{left:42px;top:468px;font-size:22px;font-weight:500;color:var(--blue);letter-spacing:.2px;white-space:nowrap}

  .photo-frame{left:566px;top:410px;width:234px;height:286px;background:var(--white);padding:5px 0 5px 5px}
  .photo-crew{width:100%;height:100%;background:linear-gradient(180deg,#3d7cc9 0%,#7fb0e3 38%,#c4c8cc 55%,#e8eaec 100%)}

  /* info columns */
  .info-icon{width:44px;height:44px;border:2px solid var(--navy);background:var(--white);display:flex;align-items:center;justify-content:center}
  .info-icon .inner{width:34px;height:34px;background:var(--navy);display:flex;align-items:center;justify-content:center}
  .info-text{font-size:12.4px;line-height:1.2}

  /* problems */
  .problems-box{left:0;top:742px;width:418px;height:296px;background:var(--panel-grey);border-radius:0 6px 6px 0}
  .problems-title{left:48px;top:730px;font-size:22px;font-weight:500;color:var(--white);letter-spacing:.4px}
  .problems-list{left:40px;top:778px;width:365px;list-style:none}
  .problems-list li{display:flex;gap:10px;font-size:13.4px;line-height:1.2;margin-bottom:15px}
  .problems-list svg{flex:none;margin-top:2px}

  /* safety */
  .safety-bar{left:435px;top:734px;width:4px;height:58px;background:var(--navy)}
  .safety-lead{left:448px;top:734px;font-size:16.5px;color:var(--navy);letter-spacing:.2px;white-space:nowrap}
  .safety-title{left:448px;top:757px;font-size:34px;line-height:1;color:var(--green)}
  .safety-list{left:448px;top:808px;width:310px;list-style:none}
  .safety-list li{display:flex;gap:14px;font-size:12.6px;line-height:1.2;margin-bottom:22px}
  .safety-list svg{flex:none}

  /* goal */
  .goal-bar{left:35px;top:1046px;width:730px;height:41px;background:var(--blue);border-radius:6px;color:var(--white);font-size:22px;line-height:41px;text-align:center;letter-spacing:.1px;overflow:hidden}

  /* footer */
  .footer-art{left:0;top:1094px}
  .footer-more{left:38px;top:1106px;color:var(--white)}
  .footer-more h3{font-size:20px;line-height:1.05}
  .footer-more p{font-size:12.5px;line-height:1.2}
  .footer-divider{left:198px;top:1112px;width:2px;height:52px;background:var(--white)}
  .footer-call{left:212px;top:1104px;color:var(--white)}
  .footer-call .label{font-size:18px;letter-spacing:.3px}
  .footer-call .phone{display:flex;align-items:center;gap:8px;font-size:25px;font-weight:600;letter-spacing:.5px;white-space:nowrap}
  .footer-contact{left:503px;top:1102px;color:var(--ink);font-size:15px;font-weight:600;line-height:1.15;font-style:normal}
  .footer-contact .row{display:flex;gap:10px;align-items:flex-start}
  .footer-contact .web{letter-spacing:2.2px;margin-top:4px}
</style>
</head>
<body>
<main class="flyer">

  <svg class="abs header-art" width="800" height="470" viewBox="0 0 800 470">
    <defs>
      <linearGradient id="towerTones" x1="0" y1="0" x2="0" y2="1">
        <stop offset="0" stop-color="#8c8f92"/>
        <stop offset=".45" stop-color="#a9adb1"/>
        <stop offset=".8" stop-color="#6f8c5b"/>
        <stop offset="1" stop-color="#9aa2a6"/>
      </linearGradient>
    </defs>
    <polygon points="382,164 612,48 800,150 800,460 382,460" fill="url(#towerTones)" role="img" aria-label="Aerial photo of a downtown tower roof with surrounding buildings and trees"/>
    <polyline points="0,155 380,155 612,38 800,140" fill="none" stroke="var(--navy)" stroke-width="7"/>
    <polyline points="0,164 382,164 612,48 800,150" fill="none" stroke="var(--white)" stroke-width="4"/>
  </svg>

  <div class="abs brand">
    <span class="brand-dot"></span>
    <span class="brand-name">Lonestar Canopy Services, INC</span>
  </div>

  <section class="abs hero-panel">
    <div class="display hero-kicker">STATE OF THE</div>
    <div class="display hero-title">ART ROOFING</div>
    <div class="display hero-sub">UNIQUE DESIGN &amp; INSTALLATION</div>
    <div class="hero-rule"></div>
    <p class="hero-copy">The Right Team, delivering innovative solutions, quality work safely for your Commercial Roofing needs.</p>
  </section>

  <svg class="abs info-band" width="800" height="44" viewBox="0 0 800 44" aria-hidden="true">
    <defs>
      <linearGradient id="bandTone" x1="0" x2="1">
        <stop offset="0" stop-color="#f4f5f7"/>
        <stop offset="1" stop-color="#c9cdd3"/>
      </linearGradient>
    </defs>
    <polygon points="0,0 528,0 548,44 0,44" fill="url(#bandTone)"/>
    <polygon points="534,0 544,0 564,44 554,44" fill="var(--band-grey)"/>
    <polygon points="548,10 568,10 568,22 554,22" fill="var(--navy)"/>
  </svg>
  <h2 class="abs info-band-title">PERTINENT INFO FOR ROOF ANCHORS</h2>

  <div class="abs photo-frame">
    <div class="photo-crew" role="img" aria-label="Photo of three roofing crew members in safety vests on a rooftop with the city skyline behind"></div>
  </div>

  <div class="abs info-icon" style="left:36px;top:518px">
    <div class="inner">
      <svg width="22" height="22" viewBox="0 0 22 22"><rect x="2" y="4" width="7" height="16" fill="#fff"/><rect x="11" y="8" width="9" height="12" fill="#fff"/><g fill="var(--navy)"><rect x="4" y="7" width="3" height="2"/><rect x="4" y="11" width="3" height="2"/><rect x="4" y="15" width="3" height="2"/><rect x="13" y="11" width="2" height="2"/><rect x="16" y="11" width="2" height="2"/><rect x="13" y="15" width="2" height="2"/><rect x="16" y="15" width="2" height="2"/></g></svg>
    </div>
  </div>
  <p class="abs info-text" style="left:95px;top:522px;width:180px">The most important thing (fairly new), if there is an accident on a building, the building owner is responsible for that accident. Previously it fell on the property manager.</p>

  <div class="abs info-icon" style="left:36px;top:640px">
    <div class="inner">
      <svg width="22" height="22" viewBox="0 0 22 22"><polygon points="2,14 14,5 20,9 8,18" fill="#fff"/><polygon points="6,14 14,8 16,10 8,16" fill="var(--navy)"/></svg>
    </div>
  </div>
  <p class="abs info-text" style="left:95px;top:644px;width:170px">Skylights are a fall-hazard to consider. Roof hatches as well.</p>

  <div class="abs info-icon" style="left:294px;top:518px">
    <div class="inner">
      <svg width="22" height="22" viewBox="0 0 22 22"><circle cx="8" cy="8" r="5" fill="none" stroke="#fff" stroke-width="2.5" stroke-dasharray="2.5 1.5"/><circle cx="8" cy="8" r="1.6" fill="#fff"/><circle cx="15" cy="15" r="4" fill="none" stroke="#fff" stroke-width="2.5" stroke-dasharray="2 1.5"/><circle cx="15" cy="15" r="1.2" fill="#fff"/></svg>
    </div>
  </div>
  <p class="abs info-text" style="left:353px;top:521px;width:190px">OSHA guidelines outlined it. Anything with mechanical equipment or any work within 15 feet of a building edge over 6 feet off the ground. Either guard rails or roof anchors. Its all dependent on your specific situation which is where we come into play. We can make that assessment.</p>

  <div class="abs problems-box"></div>
  <svg class="abs" style="left:35px;top:726px" width="182" height="34" viewBox="0 0 182 34" aria-hidden="true">
    <polygon points="0,0 152,0 170,34 0,34" fill="var(--blue)"/>
    <polygon points="156,0 162,0 180,34 174,34" fill="var(--blue)"/>
  </svg>
  <h2 class="abs problems-title">PROBLEMS</h2>

  <ul class="abs problems-list">
    <li><svg width="18" height="16" viewBox="0 0 18 16"><polygon points="9,0 18,16 0,16" fill="var(--alert)"/><rect x="8" y="5" width="2" height="6" fill="#fff"/><rect x="8" y="12" width="2" height="2" fill="#fff"/></svg><span>Falls are the leading cause of death in the construction industry.</span></li>
    <li><svg width="18" height="16" viewBox="0 0 18 16"><polygon points="9,0 18,16 0,16" fill="var(--alert)"/><rect x="8" y="5" width="2" height="6" fill="#fff"/><rect x="8" y="12" width="2" height="2" fill="#fff"/></svg><span>Roofers encounter many hazards on the job, including dangers associated with working at great heights with power tools, electricity, noise, and extreme temperatures.</span></li>
    <li><svg width="18" height="16" viewBox="0 0 18 16"><polygon points="9,0 18,16 0,16" fill="var(--alert)"/><rect x="8" y="5" width="2" height="6" fill="#fff"/><rect x="8" y="12" width="2" height="2" fill="#fff"/></svg><span>A lack of fall protection, damaged fall protection equipment, or improper setup can drastically increase a roofer’s risk of falling.</span></li>
    <li><svg width="18" height="16" viewBox="0 0 18 16"><polygon points="9,0 18,16 0,16" fill="var(--alert)"/><rect x="8" y="5" width="2" height="6" fill="#fff"/><rect x="8" y="12" width="2" height="2" fill="#fff"/></svg><span>Unless these hazards are mitigated by the property owner or employer, roofers are at risk for serious injury or death.</span></li>
  </ul>

  <div class="abs safety-bar"></div>
  <p class="abs safety-lead">AT LONESTAR CANOPY SERVICES,</p>
  <h2 class="abs display safety-title">SAFETY IS OUR MAIN PRIORITY.</h2>
  <ul class="abs safety-list">
    <li><svg width="22" height="22" viewBox="0 0 22 22"><rect x="1" y="8" width="10" height="12" fill="var(--green)"/><rect x="11" y="2" width="9" height="9" fill="var(--green)" opacity=".8"/><circle cx="11" cy="14" r="2.5" fill="#fff"/></svg><span>These areas include evidence of rooftop anchorage to provide safe access to your roof, fall protection systems to allow employees and workers to safely operate on your roof, and protection around fall hazards on your rooftop such as skylights, mechanical or ladder areas.</span></li>
    <li><svg width="22" height="22" viewBox="0 0 22 22"><rect x="1" y="8" width="10" height="12" fill="var(--green)"/><rect x="11" y="2" width="9" height="9" fill="var(--green)" opacity=".8"/><circle cx="11" cy="14" r="2.5" fill="#fff"/></svg><span>Following our inspection, our team will thoroughly review and recommend a fall prevention plan that is tailored to your specific needs.</span></li>
  </ul>

  <div class="abs display goal-bar">OUR GOAL IS TO PROVIDE YOU WITH A SYSTEM THAT IS SAFE, OSHA COMPLIANT, AND EASY TO USE.</div>

  <svg class="abs footer-art" width="800" height="106" viewBox="0 0 800 106" aria-hidden="true">
    <polygon points="0,0 428,0 496,106 0,106" fill="var(--navy)"/>
    <polygon points="484,88 800,88 800,106 496,106" fill="var(--navy)"/>
  </svg>
  <div class="abs footer-more">
    <h3 class="display">FOR MORE INFORMATION</h3>
    <p>on how we can ensure<br>the safety of your roof,</p>
  </div>
  <div class="abs footer-divider"></div>
  <div class="abs footer-call">
    <div class="label">CALL US TODAY!</div>
    <div class="phone">
      <svg width="22" height="22" viewBox="0 0 22 22" aria-hidden="true"><path d="M5 2 L9 6 L7 9 C8 12 10 14 13 15 L16 13 L20 17 L17 20 C9 20 2 13 2 5 Z" fill="#fff"/></svg>
      <span>(972) 555-0148</span>
    </div>
  </div>
  <address class="abs footer-contact">
    <div class="row">
      <svg width="16" height="20" viewBox="0 0 16 20" aria-hidden="true"><path d="M8 0 C3.6 0 1 3 1 7 C1 12 8 19 8 19 C8 19 15 12 15 7 C15 3 12.4 0 8 0 Z" fill="var(--blue)"/><circle cx="8" cy="7" r="2.6" fill="#fff"/></svg>
      <span>415 MESA RIDGE DR RICHARDSON,<br>TX 75080</span>
    </div>
    <div class="row web">
      <svg width="16" height="16" viewBox="0 0 16 16" aria-hidden="true"><circle cx="8" cy="8" r="7" fill="var(--blue)"/><ellipse cx="8" cy="8" rx="3" ry="7" fill="none" stroke="#fff" stroke-width="1.2"/><line x1="1" y1="8" x2="15" y2="8" stroke="#fff" stroke-width="1.2"/></svg>
      <span>WWW.BRELLWAYTOPS.COM</span>
    </div>
  </address>

</main>
</body>
</html>
```